Ferris Contracting LLC Business Card Design

I am looking for a creative and unique business card design. We are a commercial construction general contractor. With the name "FERRIS" Contracting, I am hoping to see some neat designs that correlate with the name.

```html
<!DOCTYPE html>
<html lang="en">
<head>
<meta charset="utf-8">
<title>Ferris Contracting LLC – Business Card</title>
<link rel="stylesheet" href="https://fonts.googleapis.com/css2?family=Montserrat:wght@400;600;700;800&display=swap">
<style>
  :root {
    --page-bg: #e6e7e9;
    --card-black: #0d0e10;
    --brand-blue: #1f9be0;
    --brand-blue-deep: #1577bd;
    --steel-light: #f2f3f5;
    --steel-mid: #b9bdc3;
    --steel-dark: #7d838b;
    --text-white: #f4f5f7;
  }
  * { margin: 0; padding: 0; box-sizing: border-box; }
  html, body {
    width: 1200px;
    height: 686px;
    overflow: hidden;
    background: var(--page-bg);
    font-family: "Montserrat", Arial, sans-serif;
  }
  .canvas {
    position: relative;
    width: 1200px;
    height: 686px;
    display: flex;
    align-items: center;
    justify-content: center;
    gap: 40px;
  }
  .card {
    position: relative;
    width: 540px;
    height: 309px;
    background: var(--card-black);
    border-radius: 4px;
    overflow: hidden;
    box-shadow: 0 6px 18px rgba(0, 0, 0, 0.18);
  }

  /* Front */
  .card-front {
    display: flex;
    align-items: center;
    justify-content: center;
  }
  .brand-name {
    color: var(--brand-blue);
    font-weight: 800;
    font-size: 40px;
    letter-spacing: 3px;
    text-transform: uppercase;
    text-align: center;
    line-height: 1.15;
  }
  .brand-name .brand-sub {
    display: block;
    font-size: 22px;
    letter-spacing: 9px;
  }

  /* Back */
  .blade-band {
    position: absolute;
    inset: 0;
    width: 100%;
    height: 100%;
  }
  .contact-block {
    position: absolute;
    left: 34px;
    top: 30px;
    color: var(--text-white);
  }
  .person-name {
    font-weight: 600;
    font-size: 22px;
    letter-spacing: 1.5px;
    text-transform: uppercase;
  }
  .person-role {
    color: var(--brand-blue);
    font-size: 12px;
    font-weight: 400;
    letter-spacing: 0.5px;
    margin-top: 1px;
  }
  .contact-list {
    list-style: none;
    margin-top: 22px;
  }
  .contact-item {
    display: flex;
    align-items: center;
    gap: 12px;
    font-size: 15px;
    letter-spacing: 0.8px;
    margin-bottom: 13px;
  }
  .contact-icon {
    width: 20px;
    height: 20px;
    border-radius: 50%;
    background: var(--brand-blue);
    display: flex;
    align-items: center;
    justify-content: center;
    flex-shrink: 0;
  }
  .contact-icon svg { width: 12px; height: 12px; }
</style>
</head>
<body>
<main class="canvas">

  <section class="card card-front" aria-label="Business card front">
    <h1 class="brand-name">Ferris<span class="brand-sub">Contracting</span></h1>
  </section>

  <section class="card card-back" aria-label="Business card back">
    <svg class="blade-band" viewBox="0 0 540 309" preserveAspectRatio="none" aria-hidden="true">
      <defs>
        <linearGradient id="steel" x1="0" y1="0" x2="1" y2="1">
          <stop offset="0" stop-color="var(--steel-dark)"/>
          <stop offset="0.45" stop-color="var(--steel-light)"/>
          <stop offset="1" stop-color="var(--steel-mid)"/>
        </linearGradient>
        <linearGradient id="blueFill" x1="0" y1="0" x2="1" y2="1">
          <stop offset="0" stop-color="var(--brand-blue)"/>
          <stop offset="1" stop-color="var(--brand-blue-deep)"/>
        </linearGradient>
      </defs>
      <path d="M352,0 Q330,215 232,309 L300,309 Q372,215 392,0 Z" fill="url(#steel)"/>
      <path d="M392,0 Q372,215 300,309 L540,309 L540,0 Z" fill="url(#blueFill)"/>
    </svg>

    <div class="contact-block">
      <h2 class="person-name">Marcus Hale</h2>
      <p class="person-role">Ceo &amp; Founder</p>
      <ul class="contact-list">
        <li class="contact-item">
          <span class="contact-icon">
            <svg viewBox="0 0 24 24" fill="#fff"><path d="M6.6 10.8a15.1 15.1 0 0 0 6.6 6.6l2.2-2.2a1 1 0 0 1 1-.25 11.4 11.4 0 0 0 3.6.57 1 1 0 0 1 1 1V20a1 1 0 0 1-1 1A17 17 0 0 1 3 4a1 1 0 0 1 1-1h3.5a1 1 0 0 1 1 1c0 1.25.2 2.45.57 3.57a1 1 0 0 1-.25 1z"/></svg>
          </span>
          222-555-0148
        </li>
        <li class="contact-item">
          <span class="contact-icon">
            <svg viewBox="0 0 24 24" fill="none" stroke="#fff" stroke-width="2"><circle cx="12" cy="12" r="9"/><path d="M3 12h18M12 3c3 3 3 15 0 18M12 3c-3 3-3 15 0 18"/></svg>
          </span>
          m.hale@ferriscontracting.com
        </li>
        <li class="contact-item">
          <span class="contact-icon">
            <svg viewBox="0 0 24 24" fill="none" stroke="#fff" stroke-width="2.2"><circle cx="12" cy="12" r="4"/><path d="M16 8v5a3 3 0 0 0 5 0v-1a9 9 0 1 0-4 7.5"/></svg>
          </span>
          www.ferriscontracting.com
        </li>
      </ul>
    </div>
  </section>

</main>
</body>
</html>
```